Premium Lawn fertiliser packaging - Looking for long term designer

*Update at bottom
I need a carefully considered, bold and professional packaging design for my new premium lawn fertiliser product. This contest is for a detailed front of the stand-up pouch packaging and once I’ve chosen a winner, they’ll be asked to create the layout for the back that links to the front as well. I have a full range of additional products that will also need designs and so I'm looking for someone who can do a great job here and who we can work with long term.

The front should include our logo for Pemberly Turf Supply Direct and be titled “Bloom Vigor Max” "Professional Lawn Fertiliser". The spring fertiliser tag line is "Wake your turf: Rich Colour, Deep Roots All Season".
Beneath it, it then needs to include some important usage information and the key benefits along with some suitable graphic.

Key information to include:

Apply March - June
Treats 35-50 m2
16-3-8
+2%MgO + 1% Fe + 2.9% CaO (this is the chemical makeup of the fertiliser and needs to be fairly prominent. If you look at other professional fertiliser packaging, you'll see how it needs to compare).

Key features:
Premium fertiliser, used by professionals
Advanced greening with micro-nutrient complex
Dual action Nitrogen: Instant green boost & continuous feed for 3 months
Child & pet safe

Our brand colours are purple and green. Purple = #592999, Green = 3cb64a / 81d742 / 4d9d44

I think these colours look great against a white background.

Please make sure you look at our website as well to get an idea of our brand: www.pemberlyturfsupply.co.uk

To help, I've attached images of competitors fertiliser packaging that I like the look of. I'm not looking for you to copy but just see what type of thing appeals to me, the standard I'm expecting and what I need to compete against....

In addition, I have also attached some potential images you may wish to try using in your design, although please feel free to use your own if you have something better. For the moment, the images are 'preview' images, but once I decide on a design and we agree on the correct image, I will download and send over a fully licensed version.

*** Update*** When submitting your design, can you submit it in 2 formats: The first as a fully printed custom stand-up pouch and the second as a full-size label stuck onto a standup pouch (whatever colour you think is right for your design - choose white if you are not sure). To explain, I've just discovered we won't be able to get full custom bags printed in time for the first run and so we will have to opt for the design to be printed on labels and fixed onto bags. I therefore need to choose a design that works in both formats as both a label on a standup pouch as well as a fully printed pouch. Many thanks.

Target Market(s)

Domestic home-owners

Industry/Entity Type

Lawn care. NOT AGRICULTURE OR FARMING

Font styles to use
Sans Serif

Requirements
Must have
• Presented in 2 formats - see update at bottom of description
Nice to have
• I quite like designs against a white background, although I’m open to other ideas as well.
Should not have
• Please do not include any people or faces in the design. The text should be solid in colour, so no graduated colour fill in the text or outline text. Please avoid over-busy or cluttered designs.

```html
<!DOCTYPE html>
<html lang="en">
<head>
<meta charset="utf-8">
<title>Bloom Vigor Max – Professional Lawn Fertiliser</title>
<link href="https://fonts.googleapis.com/css2?family=Anton&family=Fondamento&family=Montserrat:wght@600;700;800&family=Oswald:wght@500;600&family=Amatic+SC:wght@700&family=Roboto+Condensed:wght@500;700&display=swap" rel="stylesheet">
<style>
  :root{
    --purple:#592999;
    --purple-soft:#7b46b3;
    --green:#3cb64a;
    --green-lime:#81d742;
    --green-deep:#4d9d44;
    --green-dark:#1f6a2a;
    --white:#ffffff;
    --canvas:#eceeea;
    --ink:#2f3a2c;
  }
  *{box-sizing:border-box;margin:0;padding:0}
  html,body{width:1200px;height:1132px;overflow:hidden;background:var(--canvas)}
  .canvas{position:relative;width:1200px;height:1132px}
  .pouch{
    position:absolute;left:248px;top:16px;width:704px;height:1100px;
    background:var(--white);border-radius:10px;overflow:hidden;
    box-shadow:0 2px 10px rgba(0,0,0,.12);
  }
  .brand{
    position:absolute;left:0;right:0;top:120px;display:flex;justify-content:center;align-items:center;gap:12px;
  }
  .brand-dot{width:30px;height:30px;border-radius:50%;background:var(--green)}
  .brand-name{font-family:"Montserrat",sans-serif;font-weight:700;font-size:22px;color:var(--green-dark);letter-spacing:.5px}
  .title-top{
    position:absolute;left:105px;top:210px;font-family:"Fondamento",cursive;font-size:66px;line-height:1;color:var(--purple-soft);
  }
  .title-main{
    position:absolute;left:103px;top:262px;font-family:"Anton",sans-serif;font-size:118px;line-height:1;color:var(--green-lime);letter-spacing:1px;
  }
  .title-main .max{color:var(--green);font-size:132px}
  .band-line{position:absolute;left:15px;right:15px;top:412px;height:3px;background:var(--purple-soft)}
  .band{
    position:absolute;left:105px;top:391px;width:451px;height:46px;border-radius:8px;background:var(--purple-soft);
    color:var(--white);font-family:"Roboto Condensed",sans-serif;font-weight:700;font-size:30px;line-height:46px;text-align:center;
  }
  .tagline{
    position:absolute;left:0;right:0;top:448px;text-align:center;font-family:"Amatic SC",cursive;font-weight:700;font-size:24px;color:var(--purple-soft);letter-spacing:.5px;
  }
  .usage{position:absolute;left:169px;top:494px;width:342px;height:170px}
  .usage-bubble{position:absolute;inset:0}
  .usage-text{
    position:absolute;left:40px;top:26px;color:var(--white);font-family:"Montserrat",sans-serif;font-weight:700;font-size:23px;line-height:28px;
    text-shadow:0 1px 2px rgba(0,60,0,.45);
  }
  .usage-text .mix{font-size:14px;font-weight:800;line-height:22px}
  .scene{
    position:absolute;left:0;right:0;top:650px;bottom:0;
    background:linear-gradient(180deg,#bfe3f2 0%,#9ccbe0 6%,#6f9a4a 12%,#3f7a2f 24%,#5aa832 34%,#77c23c 55%,#5fae2f 80%,#4e9a27 100%);
  }
  .dual{
    position:absolute;left:242px;top:732px;width:224px;height:52px;background:var(--purple-soft);border-radius:3px;padding:5px 6px;
    color:var(--white);font-family:"Montserrat",sans-serif;
  }
  .dual-head{font-weight:800;font-size:12.5px;text-align:center}
  .dual-body{margin-top:3px;background:var(--white);color:var(--purple);font-weight:700;font-size:8.2px;line-height:10px;padding:2px 4px}
  .feature{position:absolute;top:795px;width:100px;text-align:center}
  .feature-icon{width:62px;height:62px;margin:0 auto;border-radius:50%;background:var(--purple-soft);border:3px solid rgba(255,255,255,.7);display:flex;align-items:center;justify-content:center}
  .feature-label{margin-top:6px;font-family:"Oswald",sans-serif;font-weight:500;font-size:11.5px;line-height:13px;color:var(--white);text-transform:uppercase;text-shadow:0 1px 2px rgba(0,0,0,.4)}
  .safe{position:absolute;left:82px;top:894px;width:73px;height:92px}
  .safe-text{
    position:absolute;left:7px;top:27px;width:59px;text-align:center;font-family:"Montserrat",sans-serif;font-weight:800;font-size:8.5px;line-height:10px;color:var(--ink);
  }
  .coverage{
    position:absolute;left:513px;top:912px;width:132px;height:96px;background:var(--green-dark);border:2px solid var(--green-deep);
    color:#e6f3e0;font-family:"Roboto Condensed",sans-serif;text-align:center;padding-top:6px;
  }
  .coverage-small{font-size:12px;font-weight:500;line-height:13px}
  .coverage-weight{font-size:14px;font-weight:700;line-height:15px}
  .coverage-big{font-size:19px;font-weight:700;line-height:20px}
  .coverage-rule{height:2px;background:var(--green-deep);margin:5px 0 4px}
</style>
</head>
<body>
<div class="canvas">
  <div class="pouch">
    <div class="brand">
      <span class="brand-dot"></span>
      <span class="brand-name">Pemberly Turf Supply Direct</span>
    </div>

    <div class="title-top">Bloom</div>
    <div class="title-main">VIGOR<span class="max">MAX</span></div>

    <div class="band-line"></div>
    <div class="band">PROFESSIONAL LAWN FERTILISER</div>
    <div class="tagline">"Wake your turf: rich colour, deep roots all season".</div>

    <div class="scene" role="img" aria-label="Photograph of a striped green lawn in front of a large house and trees"></div>

    <div class="usage">
      <svg class="usage-bubble" viewBox="0 0 342 170" role="img" aria-label="Grass-textured speech bubble">
        <defs>
          <linearGradient id="grass" x1="0" y1="0" x2="0" y2="1">
            <stop offset="0" stop-color="#6fcf3a"/>
            <stop offset="1" stop-color="#3e9e2a"/>
          </linearGradient>
        </defs>
        <path d="M6 8 H336 V136 H80 L62 168 L60 136 H6 Z" fill="url(#grass)"/>
      </svg>
      <div class="usage-text">
        APPLY MARCH - JUNE<br>
        TREATS 35 - 50 M2<br>
        16 - 3 - 8<br>
        <span class="mix">+2%MGO + 1% FE + 2.9% CAO</span>
      </div>
    </div>

    <div class="dual">
      <div class="dual-head">DUAL ACTION NITROGEN:</div>
      <div class="dual-body">INSTANT GREEN BOOST &amp; CONTINUOUS FEED FOR 3 MONTHS</div>
    </div>

    <div class="feature" style="left:158px">
      <div class="feature-icon">
        <svg width="32" height="32" viewBox="0 0 32 32"><path d="M16 28V15" stroke="#fff" stroke-width="2.5"/><path d="M16 16C16 9 10 6 4 7c0 6 5 10 12 9z M16 14c1-6 6-9 12-8-1 6-6 9-12 8z" fill="#fff"/><path d="M8 28h16" stroke="#fff" stroke-width="2.5"/></svg>
      </div>
      <div class="feature-label">Premium<br>Fertiliser</div>
    </div>
    <div class="feature" style="left:244px">
      <div class="feature-icon">
        <svg width="32" height="32" viewBox="0 0 32 32"><path d="M16 4l3.5 7.5 8 1-6 5.5 1.6 8L16 22l-7.1 4 1.6-8-6-5.5 8-1z" fill="#fff"/></svg>
      </div>
      <div class="feature-label">Used by<br>Professionals</div>
    </div>
    <div class="feature" style="left:332px">
      <div class="feature-icon">
        <svg width="32" height="32" viewBox="0 0 32 32"><path d="M16 3l11 4v8c0 7-5 12-11 14C10 27 5 22 5 15V7z" fill="none" stroke="#fff" stroke-width="2.5"/><path d="M11 19c2-7 7-8 11-8-1 5-4 9-11 8z" fill="#fff"/></svg>
      </div>
      <div class="feature-label">Advanced<br>Greening</div>
    </div>
    <div class="feature" style="left:420px">
      <div class="feature-icon">
        <svg width="32" height="32" viewBox="0 0 32 32" fill="#fff"><circle cx="16" cy="8" r="4"/><circle cx="7" cy="17" r="3.5"/><circle cx="25" cy="17" r="3.5"/><circle cx="16" cy="25" r="3.5"/><path d="M16 8L7 17M16 8l9 9M7 17l9 8M25 17l-9 8" stroke="#fff" stroke-width="2"/></svg>
      </div>
      <div class="feature-label">With Micro-<br>Nutrient Complex</div>
    </div>

    <div class="safe">
      <svg width="73" height="92" viewBox="0 0 73 92"><path d="M36.5 2a34 34 0 0 1 10 66.5L36.5 90 26.5 68.5A34 34 0 0 1 36.5 2z" fill="#f4f4f4" stroke="#bdbdbd" stroke-width="2"/><circle cx="36.5" cy="36" r="27" fill="none" stroke="#333" stroke-width="1.5"/></svg>
      <div class="safe-text">CHILD<br>AND PET<br>SAFE</div>
    </div>

    <div class="coverage">
      <div class="coverage-small">COVERS UP TO</div>
      <div class="coverage-big">1,000 SQ FT</div>
      <div class="coverage-rule"></div>
      <div class="coverage-small">NET WT.</div>
      <div class="coverage-weight">10 LBS /4.54 KG</div>
    </div>
  </div>
</div>
</body>
</html>
```